Professional, Elegant, Modern and Playful stationery design for an Orthodontist (Dentist)

We need a new stationery design for an Orthodontist (Dentist).
We would like to see designs that are elegant, but also playful. The designs and colors should be in harmony with the existing logo (uploaded).
The font of the logo text is roboto (Google), you don't need to use the same font, but the used font has to be in harmony with the font used in the logo and it has to be usable in Microsoft Word.
The colors used have to be in harmony with the logo.
The design for following parts are needed:
- A4 letter paper design
- A4 Microsoft Word Template (with and without letterhead)
- Envelope designs for C4 and C5 with the window on the right side
- CD/DVD-label design
- Stamping design

Target Market(s)

Orthodontist (Dentist)

Industry/Entity Type

It Professional

Font styles to use
Sans Serif

Colors

Designer to choose colors to be used in the design.

Requirements
Must have
• * Logo files are uploaded
• * A4 letter paper design: for printing press
• - Address position is on the right side
• - Needed Information in the letterhead:
• - Logo with company name as a unit
• or
• - separate the logo from the text and position them separately
• - Text needed:
• Kieferorthopädie Wendelau
• Dr. med. dent. Lukas Brenner
• Fachzahnarzt für Kieferorthopädie (CH)
• Eidg. dipl. Zahnarzt, Mitglied VZB und FDT
• Hagelbachweg 14
• 8907 Talbrugg
• 044 512 37 90
• (fax:)
• 044 512 37 91
• info@wendelau-praxis.net
• www.wendelau-praxis.net
• * A4 Microsoft Word Templates:
• - an empty and undesigned text example template is uploaded
• - the address lines are already correctly positioned behind the envelope window
• - design the positions of all elements
• - choose suitable fonts, which are in harmony with the font in the logo and the letterhead and which can be used in Microsoft Word (compatible with latest version, no old versions (.doc) needed)
• - choose suitable font sizes weights and colors, which are in harmony with the font in the logo and the letterhead.
• - One version with letterhead for printing on an empty paper
• - One version without letterhead for printing on a paper with letterhead already printed in printing press
• * Envelopes C4 and C5
• - window on the right side
• - Logo with company name (see uploaded files) as a unit
• or
• - Text needed:
• Hagelbachweg 14
• 8907 Talbrugg
• * DVD/CD-label:
• or
• - Text needed:
• Hagelbachweg 14
• 8907 Talbrugg
• 044 512 37 90
• info@wendelau-praxis.net
• www.wendelau-praxis.net
• - Patient name with birth date:
• Doe John, *1.2.1999
• - Two lines of text describing the contents on the CD/DVD
• * Stamping design:
• - Logo
• - Text:
• Kieferorthopädie Wendelau GmbH
• Hagelbachweg 14
• 8907 Talbrugg
Nice to have
• -
Should not have
• - Old Microsoft Word versions (.doc)

```html
<!DOCTYPE html>
<html lang="de">
<head>
<meta charset="utf-8">
<title>CD-Label – Kieferorthopädie Wendelau</title>
<link rel="stylesheet" href="https://fonts.googleapis.com/css2?family=Open+Sans:wght@400;700&display=swap">
<style>
  :root {
    --backdrop: #b9c7ef;
    --navy: #1b2a7a;
    --rim-blue: #2d7fc4;
    --label-light: #f3f6fa;
    --label-tint: #dde5f0;
    --text-grey: #575c68;
    --hub: #e6ebf2;
  }
  html, body {
    margin: 0;
    width: 1200px;
    height: 857px;
    overflow: hidden;
    background: var(--backdrop);
  }
  .cd-label {
    display: block;
    width: 1200px;
    height: 857px;
    font-family: "Open Sans", Arial, sans-serif;
  }
  .practice-name { font-weight: 700; font-size: 30px; fill: var(--navy); }
  .practice-line { font-weight: 400; font-size: 19px; fill: var(--text-grey); }
  .contact-ring { font-weight: 400; font-size: 22px; fill: var(--text-grey); letter-spacing: 0.3px; }
  .contact-bullet { fill: var(--navy); }
</style>
</head>
<body>
<svg class="cd-label" viewBox="0 0 1200 857" xmlns="http://www.w3.org/2000/svg">
  <defs>
    <radialGradient id="label-surface" cx="0.45" cy="0.45" r="0.6">
      <stop offset="0" stop-color="var(--label-light)"/>
      <stop offset="1" stop-color="var(--label-tint)"/>
    </radialGradient>
    <path id="contact-arc" d="M 367.3 150.7 A 362 362 0 1 0 956.5 490.9"/>
  </defs>

  <circle class="disc-rim" cx="600" cy="428" r="402" fill="var(--navy)"/>
  <circle class="disc-rim-inner" cx="600" cy="428" r="396" fill="var(--rim-blue)"/>

  <circle class="label-surface" cx="600" cy="428" r="390" fill="url(#label-surface)"
          role="img" aria-label="Soft background pattern of pale blue squares"/>

  <circle class="hub" cx="600" cy="428" r="90" fill="var(--hub)" opacity="0.8"/>
  <circle class="centre-hole-ring" cx="600" cy="428" r="48" fill="#c9d2e0"/>
  <circle class="centre-hole" cx="600" cy="428" r="42" fill="var(--backdrop)"/>

  <circle class="name-mark" cx="462" cy="204" r="14" fill="var(--rim-blue)"/>
  <text class="practice-name" x="486" y="215">Kieferorthopädie Wendelau</text>
  <text class="practice-line" x="500" y="250">Dr. med. dent. Lukas Brenner</text>
  <text class="practice-line" x="500" y="278">Fachzahnarzt für Kieferorthopädie (CH)</text>
  <text class="practice-line" x="500" y="306">Eidg. dipl. Zahnarzt, Mitglied VZB und FDT</text>

  <text class="contact-ring">
    <textPath href="#contact-arc">
      <tspan class="contact-bullet">●</tspan> Hagelbachweg 14, 8907 Talbrugg
      <tspan class="contact-bullet">●</tspan> 044 512 37 90
      <tspan class="contact-bullet">●</tspan> 044 512 37 91
      <tspan class="contact-bullet">●</tspan> info@wendelau-praxis.net
      <tspan class="contact-bullet">●</tspan> www.wendelau-praxis.net
    </textPath>
  </text>
</svg>
</body>
</html>
```